Book Cover Design Project

I have written a booK called "keep the lamp Lit:
a guide to starting and running a small business. It is aimed at the start up entrepreneur and seeks to give them everything they need to start up and run a small business. I am interested in a very simple cover that is contemporary in the look but clearly communicates the mission of the book. It should sell very well as there are no others like it, so the designer will get excellent exposure.
Updates

Reason: I an vacation in Europe until the 23rd of July. Would like a few days to make a decision after my return Walt

We are currently on vacation.  Will make a final decision in about a week.  Thanks so much for your submissions

Walt

Target Market(s)

Start up businesses in the U.S.

Industry/Entity Type

Business

Requirements
Must have
• Clear communication of the name. Lots of white space. Graphic communication of the purpose of the book? Prominent exposure of my name. Walter j. Pennick

```html
<!DOCTYPE html>
<html lang="en">
<head>
<meta charset="utf-8">
<title>Keep the Lamp Lit — Book Cover</title>
<link rel="stylesheet" href="https://fonts.googleapis.com/css2?family=Cinzel:wght@400;500&family=Oswald:wght@600;700&display=swap">
<style>
  :root {
    --canvas-bg: #ecebe8;
    --cover-light: #ffffff;
    --cover-mid: #f1f1f1;
    --cover-edge: #dcdcdc;
    --ink-dark: #1e1e1e;
    --title-top: #1f5fb0;
    --title-bottom: #0a3a86;
    --art-green-light: #9fdc5a;
    --art-green-dark: #2f8f1e;
  }
  * { margin: 0; padding: 0; box-sizing: border-box; }
  html, body {
    width: 1200px;
    height: 1035px;
    overflow: hidden;
    background: var(--canvas-bg);
  }
  .canvas {
    position: relative;
    width: 1200px;
    height: 1035px;
  }
  .book-cover {
    position: absolute;
    left: 300px;
    top: 38px;
    width: 600px;
    height: 960px;
    background: radial-gradient(ellipse at 50% 70%, var(--cover-light) 0%, var(--cover-mid) 55%, var(--cover-edge) 100%);
    box-shadow: 0 6px 24px rgba(0,0,0,0.18);
    text-align: center;
  }
  .author-name {
    position: absolute;
    top: 40px;
    left: 0;
    width: 100%;
    font-family: "Cinzel", serif;
    font-weight: 400;
    font-size: 46px;
    letter-spacing: 1px;
    color: var(--ink-dark);
  }
  .book-title {
    position: absolute;
    top: 118px;
    left: 0;
    width: 100%;
    font-family: "Oswald", sans-serif;
    font-weight: 700;
    font-size: 150px;
    line-height: 1.02;
    text-transform: uppercase;
    letter-spacing: -1px;
    background: linear-gradient(180deg, var(--title-top), var(--title-bottom));
    -webkit-background-clip: text;
    background-clip: text;
    color: transparent;
  }
  .book-title span { display: block; }
  .cover-art {
    position: absolute;
    left: 170px;
    top: 500px;
    width: 260px;
    height: 300px;
    border-radius: 50%;
    background: radial-gradient(circle at 50% 50%, var(--art-green-light) 0%, var(--art-green-dark) 45%, rgba(255,255,255,0) 72%);
  }
  .subtitle {
    position: absolute;
    top: 818px;
    left: 0;
    width: 100%;
    font-family: "Cinzel", serif;
    font-weight: 400;
    font-size: 31px;
    line-height: 62px;
    color: var(--ink-dark);
  }
</style>
</head>
<body>
  <main class="canvas">
    <section class="book-cover">
      <p class="author-name">Walter J. Pennick</p>
      <h1 class="book-title"><span>Keep the</span><span>Lamp Lit</span></h1>
      <div class="cover-art" role="img" aria-label="Green dollar sign with sprouting leaves, symbolising a growing business"></div>
      <p class="subtitle">A GUIDE TO STARTING AND<br>RUNNING A SMALL BUSINESS</p>
    </section>
  </main>
</body>
</html>
```